Presentation Folder Design for Photographer

Professional photographer requires a presentation folder for marketing.
I specialise in architecture, corporate & commercial photography. The folder will be used to promote my architectural photography services to real estate, accomodation & architect clients.

I'm looking for a modern clean design that complements my logo with complimentary text & colours. I want to use some images in the design, probably a mix of images not just architectural. I need a print ready design in PDF as well as a PSD file that I can possibly edit / update images later on.

The folder will be a double sided design with no need for pockets included in the design. Overall dimensions are 430mm ( folded down the centre ) x 315mm with a 5mm trim & bleed.

The layout would be as follows :

Front cover - Logo + maybe some images or some other design work.

Inside front cover - Some text about my services.

ARCHITECTURE
Commercial Residential Real Estate Drone Floorpans Accommodation

CORPORATE
Studio Headshots Environmental Portraits Staff Photography

COMMERCIAL
Product Advertising Fashion Event Stock

Inside back cover - no text as a seperate price list will sit here.

Outside back cover - I was thinking of having a collage of images worked into
the design but open to the designers input as well.
I also have another logo with phone number & web address
I would like on the back cover - Will be included in the files
provided.

I have a black background & white background version of my logo I will include both for the design work. I'm trying to get away from an all black design so if using the black logo I don't want a completely black page design, just becomes to heavy.

I'm redoing my website soon so please base the folder design around my logo text & colours not my current website as it's very outdated.

Logo brand guide is as follows

Main Font Font: Reislust
Main Font Color: #fff
Slogan Font Font: Ubuntu Bold
Monogram Font Font: Venti Medium
Container Color: #fff

Please respect the copyright on the images provided and delete all content once the design has been completed.
Thanks.

Need extra days to review

```html
<!DOCTYPE html>
<html lang="en">
<head>
<meta charset="utf-8">
<title>Frame Line Studio – Presentation Folder</title>
<link href="https://fonts.googleapis.com/css2?family=Josefin+Sans:wght@300;400;600&display=swap" rel="stylesheet">
<style>
  :root {
    --backdrop: #d9d9d9;
    --paper: #f3f3f3;
    --paper-grey: #e4e4e4;
    --ink: #3a3a3a;
    --gold-dark: #b98f3e;
    --gold-mid: #d6b462;
    --gold-light: #f0e3a4;
  }
  * { box-sizing: border-box; margin: 0; padding: 0; }
  html, body { width: 1200px; height: 900px; overflow: hidden; }
  body {
    background: var(--backdrop);
    font-family: "Josefin Sans", sans-serif;
    color: var(--ink);
    position: relative;
  }
  .folder-spread {
    position: absolute; left: 40px; top: 40px;
    width: 1120px; height: 820px;
    display: flex;
    box-shadow: 0 10px 30px rgba(0,0,0,.18);
  }
  .panel { position: relative; width: 560px; height: 820px; overflow: hidden; }
  .panel--back { background: var(--paper-grey); }
  .panel--front { background: var(--paper); }

  .photo { position: absolute; }
  .gold-bar { position: absolute; background: linear-gradient(180deg, var(--gold-light), var(--gold-mid) 55%, var(--gold-dark)); }

  .brand { position: absolute; display: flex; align-items: center; gap: 14px; }
  .brand__mark { width: 46px; height: 46px; border: 3px solid var(--gold-mid); border-radius: 50%; flex: none; }
  .brand__name { font-weight: 400; font-size: 26px; letter-spacing: 4px; text-transform: uppercase; color: var(--ink); line-height: 1; }
  .brand__sub { font-weight: 600; font-size: 8px; letter-spacing: 1.6px; color: var(--ink); margin-top: 6px; }

  .photographer-credit {
    position: absolute; left: 0; right: 0; top: 752px;
    text-align: center; font-size: 15px; letter-spacing: 3px; text-transform: uppercase;
  }
</style>
</head>
<body>
  <div class="folder-spread">
    <!-- Outside back cover -->
    <section class="panel panel--back">
      <div class="photo" role="img" aria-label="Brick country house with blue roof and garden at dusk" style="left:0;top:0;width:560px;height:230px;background:linear-gradient(180deg,#6f8fc4 0%,#8a7a5c 55%,#4f7a3a 100%);"></div>
      <div class="photo" role="img" aria-label="White modern kitchen bench" style="left:0;top:236px;width:300px;height:94px;background:linear-gradient(180deg,#f0f0f0,#cfcfcf 70%,#3a3a3a);"></div>
      <div class="photo" role="img" aria-label="Studio portrait in pink outfit" style="left:306px;top:236px;width:144px;height:164px;background:linear-gradient(180deg,#ececec,#e8b6c6);"></div>
      <div class="photo" role="img" aria-label="Light timber kitchen with stools" style="left:456px;top:236px;width:104px;height:164px;background:linear-gradient(180deg,#f3efe8,#d9c4a2);"></div>
      <div class="photo" role="img" aria-label="Dark fashion portrait" style="left:0;top:336px;width:120px;height:134px;background:linear-gradient(180deg,#2a2a2a,#5a5a5a);"></div>
      <div class="photo" role="img" aria-label="Portrait in white tutu dress on black" style="left:126px;top:336px;width:124px;height:134px;background:radial-gradient(circle at 50% 70%,#e6e6e6,#1b1b1b 65%);"></div>
      <div class="photo" role="img" aria-label="Historic homestead at twilight" style="left:256px;top:406px;width:304px;height:104px;background:linear-gradient(180deg,#2e3e73,#6a6a78 60%,#5f6a3a);"></div>

      <div class="gold-bar" style="left:0;top:520px;width:14px;height:200px;"></div>

      <div class="brand" style="left:110px;top:600px;">
        <div class="brand__mark"></div>
        <div>
          <div class="brand__name">Frame Line Studio</div>
          <div class="brand__sub">PH 0400 118 274 &nbsp; WWW.FRAMELINESTUDIO.COM.AU</div>
        </div>
      </div>
    </section>

    <!-- Front cover -->
    <section class="panel panel--front">
      <div class="brand" style="left:150px;top:80px;">
        <div class="brand__mark"></div>
        <div>
          <div class="brand__name">Frame Line Studio</div>
          <div class="brand__sub">ARCHITECTURE CORPORATE COMMERCIAL</div>
        </div>
      </div>

      <div class="gold-bar" style="left:40px;top:210px;width:28px;height:470px;"></div>
      <div class="photo" role="img" aria-label="Bedroom with chandelier and framed pictures" style="left:92px;top:180px;width:120px;height:530px;background:linear-gradient(180deg,#b9a58e,#e6dccf 55%,#c9b7a0);"></div>
      <div class="photo" role="img" aria-label="Fashion portrait with black balloons at stone doorway" style="left:222px;top:190px;width:120px;height:530px;background:linear-gradient(180deg,#9c8a6e,#6b5a44 50%,#2b2b2b);"></div>
      <div class="photo" role="img" aria-label="Red brick mansion with purple flower garden" style="left:352px;top:200px;width:120px;height:530px;background:linear-gradient(180deg,#6d7fb8,#b0553f 40%,#6a4f8c 65%,#3f6b2e);"></div>
      <div class="gold-bar" style="left:494px;top:240px;width:28px;height:480px;"></div>

      <div class="photographer-credit">Photographer Marcus Hale</div>
    </section>
  </div>
</body>
</html>
```